Wordpress Design for Interactive Marketing Agency

We are looking to have a WP theme designed for our company, Bright Harbor Media. We are an online marketing firm specializing in SEO, Paid Search/PPC, Analytics and a number of other marketing channels.
We have a logo and tag line. We also have a rough and unloved design to work from as a way to illustrate the content needs of the homepage. We would like an interactive slider on the homepage which displays text and image content describing our services and our value props/solution positioning. Layering content is also something we'd like to incorporate in a block or two on the page, whether it be tabs, window shades, rotating or mouse-over type div swapping, scrolling news box, etc.
The design also needs to be able to transition to a less portal-like feel (re: the homepage) to a page design that houses a description for each of our services, an about page, privacy page, etc.
So, in the spirit of the typical WP construct, there would be a consistent header and footer, with a main content div that is flexible and eye-catching.
Three column design for the homepage feels right, but that's not a requirement. For the rest of the pages one or two columns seems like the right layout. Again, is this open to design.
To see what we've put together as a concept visit this page:
www.brightharbormedia.example/design/
Notes: most folks didn't care for the opaque gun in the background. Though, a subtle, muted background image would be a welcome design element. Keep in mind that these images are only for illustrating the content needs. We are not expecting anything that looks like these concepts. In fact, they didn't appeal to most of us.
Also included is a third design that we kind of liked (probably could live without the page curls, though). Modern sophistication that isn't stuffy but doesn't get too juvenile is what we're wanting. If there's a way to complement the power colors of our logo and attain a style that's lively, digerati in spirit and alluring, then that's what we would like to arrive at.
To get the latest logo:
http://brightharbormedia.example/design/Logo-Rework.png
The logo can be rearranged as needed.
I have also attached the rough designs we put together and the logo.
We really don't have any strong restrictions or absolutes as far as how the design turns out. We just want something that looks great and captures the spirit of the business/brand. The visuals could definitely benefit from a human element, or a splashy graphic or something festive, technically inclined and/or inclusive.
Updates
Project Deadline Extended
Reason: I am trying to make the project a little more accessible for designers by extending it a bit. I realize that the process can sometimes take several days, and if this allows for more submissions, there are no complaints here.
Hi Designers,
Target Market(s)
Medium-sized, regional businesses
Industry/Entity Type
Marketing
Requirements
Must have
- Theme must accomodate widgets, permalinks and all of the common WP page enhancements and taxonomy options.
Nice to have
- Most of the text on the page should be true text if possible (for SEO purposes, etc.). The ability to layer text content is also desirable, so having content blocks that use z-indexed divs would be ideal. Theme should accommodate widgets, permalinks and all of the common WP page enhancements and taxonomy options.

```html
<!DOCTYPE html>
<html lang="en">
<head>
<meta charset="utf-8">
<title>Bright Harbor Media – Online Marketing</title>
<link rel="stylesheet" href="https://fonts.googleapis.com/css2?family=Open+Sans:ital,wght@0,400;0,600;0,700;1,400&family=PT+Sans:wght@400;700&display=swap">
<style>
:root{
  --orange-top:#f2ad3a;
  --orange-bottom:#e6951c;
  --ink:#333333;
  --text:#555555;
  --brown:#7a2a00;
  --red:#d8401c;
  --black:#000000;
  --panel:#3b3b3b;
  --green:#7cbc3f;
  --green-dark:#6aaf2c;
  --yellow:#f7c600;
  --yellow-dark:#e9b400;
  --amber:#f7800f;
  --amber-dark:#ef6e06;
  --crimson:#e30000;
  --crimson-dark:#cf0000;
  --white:#ffffff;
  --rule:#dddddd;
  --input-border:#c98a5a;
}
*{box-sizing:border-box;margin:0;padding:0}
html,body{width:780px;height:1200px;overflow:hidden}
body{position:relative;background:var(--white);font-family:"Open Sans",Arial,sans-serif;color:var(--text)}
.abs{position:absolute}

/* header */
.site-header{left:0;top:0;width:780px;height:250px;background:linear-gradient(180deg,var(--orange-top),var(--orange-bottom))}
.brand{left:12px;top:12px;width:260px;height:108px;border-radius:12px;background:rgba(255,255,255,.28);display:flex;flex-direction:column;justify-content:flex-end;padding:0 0 8px 12px}
.brand-name{font-family:"PT Sans",sans-serif;font-weight:700;font-size:19px;color:#1a1a1a;letter-spacing:.3px;text-transform:uppercase;display:flex;align-items:center;gap:6px;white-space:nowrap}
.brand-dot{width:10px;height:10px;border-radius:50%;background:var(--red);flex:none}
.brand-tag{font-size:10px;font-weight:700;color:#6a6a6a;margin:1px 0 0 74px;white-space:nowrap}
.phone{left:292px;top:26px;font-family:"PT Sans",sans-serif;font-size:26px;color:#1e1e1e;letter-spacing:1px;white-space:nowrap}
.audit{left:340px;top:62px;font-family:"PT Sans",sans-serif;font-size:17px;color:#5a3300}
.social-label{left:546px;top:29px;font-family:"PT Sans",sans-serif;font-size:13px;color:var(--brown)}
.social{top:22px;width:24px;height:24px;border-radius:3px}
.social.s1{left:668px;background:#37a9e0}
.social.s2{left:706px;background:#3b5b9a}
.social.s3{left:744px;background:#f39a1e;border:1px solid #fff}
.search{left:596px;top:67px;width:174px;height:20px;display:flex}
.search-field{flex:1;background:var(--white);font-size:9px;color:#777;padding:4px 12px}
.search-btn{width:25px;background:#e01818;display:flex;align-items:center;justify-content:center}
.util-links{left:561px;top:98px;font-size:9.5px;color:var(--brown);white-space:nowrap}
.util-links span{margin:0 6px}

/* navigation */
.main-nav{left:12px;top:147px;width:759px;height:76px;background:var(--black);box-shadow:0 6px 10px rgba(0,0,0,.25)}
.nav-item{top:13px;font-family:"PT Sans",sans-serif;font-size:17px;color:var(--white);text-align:center;display:flex;flex-direction:column;align-items:center;gap:4px;white-space:nowrap}
.nav-item svg{display:block}

/* hero */
.hero{left:12px;top:250px;width:758px;height:310px;background:var(--white)}
.hero-art{left:20px;top:250px;width:550px;height:308px;background:radial-gradient(ellipse at 55% 55%,#a9cde9 0%,#d8e9f5 55%,#ffffff 80%)}
.hero-q{left:497px;top:286px;font-family:"PT Sans",sans-serif;font-size:17px;color:var(--ink)}
.hero-line{left:497px;top:325px;font-family:"PT Sans",sans-serif;font-size:17px;color:var(--ink)}
.hero-title{left:496px;top:348px;font-family:"PT Sans",sans-serif;font-size:32px;color:var(--red)}

/* contact panel */
.contact{left:38px;top:234px;width:182px;height:182px;background:var(--panel);box-shadow:3px 4px 8px rgba(0,0,0,.45);color:#eee;font-size:10px}
.contact h3{position:absolute;left:0;top:3px;width:100%;font-family:"PT Sans",sans-serif;font-weight:400;font-size:12px;color:#f0b040;text-align:center}
.contact .pin{top:3px;width:6px;height:6px;border-radius:50%;background:#9ed07a}
.contact label{position:absolute;left:9px;line-height:12px}
.contact .field{position:absolute;left:8px;width:164px;height:17px;background:var(--white)}
.contact .area{height:40px}
.contact .submit{position:absolute;left:114px;top:157px;width:53px;height:18px;background:linear-gradient(#fff,#d8d8d8);color:#b01010;font-weight:700;font-size:10px;text-align:center;line-height:18px}

/* service tiles */
.tile{top:562px;width:188px;height:107px;color:var(--white);overflow:hidden}
.tile h2{height:36px;font-family:"PT Sans",sans-serif;font-weight:400;font-size:16px;text-align:center;line-height:38px;white-space:nowrap}
.tile p{font-size:9px;line-height:14px;padding:4px 0 0 15px;white-space:nowrap}
.tile .corner{position:absolute;right:0;bottom:0;width:20px;height:20px;background:var(--white);display:flex;align-items:center;justify-content:center}
.t1{left:12px;background:var(--green)} .t1 h2{background:var(--green-dark)}
.t2{left:202px;background:var(--yellow)} .t2 h2{background:var(--yellow-dark)}
.t3{left:391px;background:var(--amber)} .t3 h2{background:var(--amber-dark)}
.t4{left:581px;width:189px;background:var(--crimson)} .t4 h2{background:var(--crimson-dark)}

/* content columns */
.welcome{left:18px;top:684px;width:330px}
.welcome h2{font-family:"PT Sans",sans-serif;font-weight:400;font-size:17px;color:var(--red);margin-bottom:6px}
.welcome p{font-size:9.3px;line-height:15.3px;text-align:justify;color:#666}
.more{font-size:9.5px;font-style:italic;color:#222}
.divider{top:690px;width:1px;height:160px;background:linear-gradient(transparent,var(--rule),transparent)}
.login{left:397px;top:692px;width:155px}
.login h2,.blog h2{font-family:"PT Sans",sans-serif;font-weight:400;font-size:17px;color:var(--ink)}
.login .input{height:26px;border:1.5px solid var(--input-border);font-size:9px;color:#555;padding:7px 6px}
.login .btn{width:60px;height:20px;border:1px solid #aaa;background:linear-gradient(#fff,#ddd);font-size:9.5px;color:#333;text-align:center;line-height:18px}
.blog{left:583px;top:692px;width:185px}
.blog ul{list-style:none;margin-top:14px}
.blog li{font-size:9.5px;color:#666;line-height:21px;padding-left:14px;position:relative;white-space:nowrap}
.blog li::before{content:"";position:absolute;left:2px;top:9px;width:5px;height:5px;background:#e09a3a}

/* projects */
.projects-title{left:0;top:895px;width:752px;text-align:center;font-family:"PT Sans",sans-serif;font-weight:400;font-size:17px;color:var(--red)}
.project{top:925px;width:247px;height:55px;border:1px solid #bbb;background:linear-gradient(#ffffff,#d9d9d9);padding:6px 10px}
.project h3{font-family:"PT Sans",sans-serif;font-weight:400;font-size:16px;color:#222;line-height:16px}
.project p{font-size:9.3px;color:#888;line-height:15px}

/* footer */
.site-footer{left:0;top:1012px;width:780px;height:158px;background:var(--black);color:var(--white)}
.news-title{left:29px;top:1055px;font-family:"PT Sans",sans-serif;font-weight:400;font-size:16px;color:var(--white)}
.news-field{left:31px;top:1081px;width:186px;height:21px;background:var(--white);font-size:9px;color:#444;padding:5px 7px}
.news-btn{left:32px;top:1120px;width:76px;height:19px;background:var(--green-dark);font-size:9px;color:#fff;text-align:center;line-height:19px}
.foot-rule{top:1031px;width:1px;height:124px;background:#3a3a3a}
.foot-links{left:314px;top:1032px;list-style:none;font-size:9.5px;color:#fff;line-height:23.3px}
.foot-brand{left:500px;top:1084px;width:236px;text-align:right}
.foot-brand .name{font-family:"PT Sans",sans-serif;font-weight:700;font-size:17px;color:var(--white);text-transform:uppercase;letter-spacing:.5px;white-space:nowrap}
.foot-brand .tag{font-size:9.5px;font-weight:700;color:var(--white)}
.foot-badge{left:648px;top:1122px;width:90px;height:36px;border-radius:4px;background:#1f6a9c}
.copyright{left:0;top:1170px;width:780px;height:30px;background:#111;border-top:1px solid #333;font-size:9px;color:#ddd;text-align:center;line-height:30px}
</style>
</head>
<body>

<header class="abs site-header" aria-label="Site header">
  <div class="abs brand">
    <div class="brand-name"><span class="brand-dot"></span>Bright Harbor Media</div>
    <div class="brand-tag">Online Marketing. ON COURSE</div>
  </div>
  <div class="abs phone">1008 – 555010-200</div>
  <div class="abs audit">GET A FREE AUDIT!</div>
  <div class="abs social-label">SOCIALIZE WITH US</div>
  <span class="abs social s1"></span>
  <span class="abs social s2"></span>
  <span class="abs social s3"></span>
  <div class="abs search">
    <div class="search-field">Enter your search</div>
    <div class="search-btn">
      <svg width="12" height="12" viewBox="0 0 12 12"><circle cx="5" cy="5" r="3.6" fill="none" stroke="#fff" stroke-width="1.6"/><line x1="7.6" y1="7.6" x2="11" y2="11" stroke="#fff" stroke-width="1.8"/></svg>
    </div>
  </div>
  <div class="abs util-links">SignIn<span>|</span>Help<span>|</span>Sitemap<span>|</span>FAQ<span>|</span>Join Us</div>
</header>

<nav class="abs main-nav" aria-label="Main">
  <div class="abs nav-item" style="left:102px">PAID SEARCH<svg width="22" height="20" viewBox="0 0 22 20"><path d="M7 0h8v9h7L11 20 0 9h7z" fill="#b0501c"/></svg></div>
  <div class="abs nav-item" style="left:240px">SEO<svg width="22" height="20" viewBox="0 0 22 20"><path d="M7 0h8v9h7L11 20 0 9h7z" fill="#b0501c"/></svg></div>
  <div class="abs nav-item" style="left:309px">DISPLAY ADS<svg width="22" height="20" viewBox="0 0 22 20"><path d="M7 0h8v9h7L11 20 0 9h7z" fill="#b0501c"/></svg></div>
  <div class="abs nav-item" style="left:445px">ANALITICS<svg width="22" height="20" viewBox="0 0 22 20"><path d="M7 0h8v9h7L11 20 0 9h7z" fill="#b0501c"/></svg></div>
  <div class="abs nav-item" style="left:563px">PERFORMANCE<svg width="22" height="20" viewBox="0 0 22 20"><path d="M7 0h8v9h7L11 20 0 9h7z" fill="#b0501c"/></svg></div>
</nav>

<section class="abs hero" aria-label="Featured service"></section>
<div class="abs hero-art" role="img" aria-label="Folded world map with a large red location pin"></div>
<p class="abs hero-q">Are you on a Map?</p>
<p class="abs hero-line">We get you there with our local</p>
<p class="abs hero-title">SEO Service</p>

<form class="abs contact" aria-label="Contact Us">
  <span class="abs pin" style="left:17px"></span>
  <span class="abs pin" style="left:157px"></span>
  <h3>Contact Us</h3>
  <label style="top:23px">Name:</label><div class="field" style="top:36px"></div>
  <label style="top:57px">E-mail:</label><div class="field" style="top:69px"></div>
  <label style="top:91px">How can we help you:</label><div class="field area" style="top:107px"></div>
  <div class="submit">SUBMIT</div>
</form>

<article class="abs tile t1"><h2>LOCAL SEO</h2><p>Lorem Ipsum is simply dummy text of<br>the printing and typesetting Lorem<br>Ipsum is simply dummy text of the<br>printing and typesetting industry.</p><span class="corner"><svg width="12" height="14" viewBox="0 0 12 14"><path d="M4 0h4v7h4L6 14 0 7h4z" fill="var(--green)"/></svg></span></article>
<article class="abs tile t2"><h2>CALL TRACKING</h2><p>Lorem Ipsum is simply dummy text of<br>the printing and typesetting Lorem<br>Ipsum is simply dummy text of the<br>printing and typesetting industry.</p><span class="corner"><svg width="12" height="14" viewBox="0 0 12 14"><path d="M4 0h4v7h4L6 14 0 7h4z" fill="var(--yellow)"/></svg></span></article>
<article class="abs tile t3"><h2>AFFILIATE MARKETING</h2><p>Lorem Ipsum is simply dummy text of<br>the printing and typesetting Lorem<br>Ipsum is simply dummy text of the<br>printing and typesetting industry.</p><span class="corner"><svg width="12" height="14" viewBox="0 0 12 14"><path d="M4 0h4v7h4L6 14 0 7h4z" fill="var(--amber)"/></svg></span></article>
<article class="abs tile t4"><h2>DEVELOPMENT</h2><p>Lorem Ipsum is simply dummy text of<br>the printing and typesetting Lorem<br>Ipsum is simply dummy text of the<br>printing and typesetting industry.</p><span class="corner"><svg width="12" height="14" viewBox="0 0 12 14"><path d="M4 0h4v7h4L6 14 0 7h4z" fill="var(--crimson)"/></svg></span></article>

<section class="abs welcome">
  <h2>Welcome</h2>
  <p>Lorem Ipsum is simply dummy text of the printing and typesetting industry. Lorem Ipsum has been the industry's standard dummy text ever since the 1500s, when an unknown printer took a galley of type and scrambled it to make a type specimen book. It has survived not only five centuries, but also the leap into electronic typesetting, remaining essentially unchanged. It was popularised in the 1960s with the release of Lettrix sheets containing Lorem Ipsum passages, and more recently with desktop publishing software like Folio PageSetter including versions of Lorem Ipsum.</p>
  <p class="more" style="text-align:right;margin-right:12px;margin-top:2px">read more...</p>
</section>
<span class="abs divider" style="left:370px"></span>
<span class="abs divider" style="left:565px"></span>

<section class="abs login">
  <h2>Login Form</h2>
  <div class="input" style="margin-top:26px">User name</div>
  <div class="input" style="margin-top:19px">Password</div>
  <div class="btn" style="margin-top:12px">Submit</div>
</section>

<section class="abs blog">
  <h2>Current Events &amp; Blog</h2>
  <ul>
    <li>Lorem Ipsum is simply dummy</li>
    <li>Posel oplop kot'is simply dummy</li>
    <li>Punu lopu folpr hoitop kolpi sipo</li>
    <li>Hundo polpu wopkudlo bolpg topko</li>
  </ul>
  <p class="more" style="text-align:right;margin-right:33px;margin-top:4px">read more...</p>
</section>

<h2 class="abs projects-title">LATEST PROJECTS</h2>
<article class="abs project" style="left:12px"><h3>PROJECT 1</h3><p>publishing software like Folio PageSetter including versions of Lorem Ipsum. <svg width="14" height="11" viewBox="0 0 14 11"><path d="M0 0h14L7 11z" fill="#555"/></svg></p></article>
<article class="abs project" style="left:268px"><h3>PROJECT 2</h3><p>publishing software like Folio PageSetter including versions of Lorem Ipsum. <svg width="14" height="11" viewBox="0 0 14 11"><path d="M0 0h14L7 11z" fill="#555"/></svg></p></article>
<article class="abs project" style="left:524px"><h3>PROJECT 3</h3><p>publishing software like Folio PageSetter including versions of Lorem Ipsum. <svg width="14" height="11" viewBox="0 0 14 11"><path d="M0 0h14L7 11z" fill="#555"/></svg></p></article>

<footer class="abs site-footer" aria-label="Site footer"></footer>
<h2 class="abs news-title">SUBSCRIBE FOR NEWSLETTER</h2>
<div class="abs news-field">enter your e-mail address</div>
<div class="abs news-btn">SUBSCRIBE</div>
<span class="abs foot-rule" style="left:274px"></span>
<span class="abs foot-rule" style="left:468px"></span>
<ul class="abs foot-links">
  <li>Privacy Policy</li>
  <li>Terms of Service</li>
  <li>About Us</li>
  <li>Contact Us</li>
  <li>Our Blog</li>
</ul>
<div class="abs foot-brand">
  <div class="name">Bright Harbor Media</div>
  <div class="tag">Online Marketing. ON COURSE</div>
</div>
<span class="abs foot-badge"></span>
<div class="abs copyright">@copyright 2012.All Rights Reserved</div>

</body>
</html>
```